Event Poster Design for Camp for Teenagers

I need graphics designed for our summer camps event. These camps are for teenagers, 6-12th grades. Primary graphic design is for a 11x17 poster but will also need the images resized for social, 16x9 title slide, and a postcard size. Graphic should include the following:Main Title: Pine Ridge Youth Summer CampsDates: High School - June 3-7; Middle School - June 17-21; Ignite - June 24 - 28Register at SDNextGen.comFor each camp, include name and headshot of speaker:High: Ray Whitcomb (guy in blue shirt)Middle: Marla Pettis (girl)Ignite: Joey SilvaInclude Pine Ridge Youth logoBlack Hills Retreat Center, Deadwood, SDGraphic should be attractive to teenagers. Ideas - geometric shapes, 90's coloring/imagery, bright colors, soft earth tones, etc. Open to ideasMy graphic design experience is VERY limited. I will need help receiving the files I need in the various sizes. Thank you.
Look and feel
Each slider illustrates characteristics of the customer's brand and the style your logo design should communicate.

```html
<!DOCTYPE html>
<html lang="en">
<head>
<meta charset="utf-8">
<title>Pine Ridge Youth Summer Camps</title>
<link rel="stylesheet" href="https://fonts.googleapis.com/css2?family=Rubik+Glitch&family=Arimo:wght@400;700&display=swap">
<style>
  :root {
    --page: #ffffff;
    --night: #06040c;
    --white: #ffffff;
    --summer-red: #e8202a;
    --camps-yellow: #fff200;
    --magenta: #c53fe0;
    --violet: #5b2bd6;
    --slate: #3a3a3e;
    --logo-blue: #2cc3f2;
  }
  * { box-sizing: border-box; margin: 0; padding: 0; }
  html, body { width: 1200px; height: 1200px; overflow: hidden; background: var(--page); }
  .poster {
    position: absolute; left: 264px; top: 125px; width: 674px; height: 953px;
    background: var(--night); overflow: hidden; color: var(--white);
    font-family: "Arimo", Arial, sans-serif;
  }
  .backdrop { position: absolute; inset: 0; width: 100%; height: 100%; }
  .title { position: absolute; left: 0; width: 100%; text-align: center; font-family: "Rubik Glitch", "Arial Black", sans-serif; line-height: 1; white-space: nowrap; }
  .title-brand { top: 62px; font-size: 42px; letter-spacing: 2px; color: var(--white); }
  .title-summer { top: 126px; font-size: 90px; color: var(--summer-red); }
  .title-camps { top: 216px; font-size: 108px; color: var(--camps-yellow); }
  .schedule { position: absolute; left: 0; width: 100%; top: 330px; text-align: center; font-size: 28px; line-height: 38px; }
  .schedule b { font-weight: 700; }
  .register { position: absolute; left: 0; width: 100%; top: 450px; text-align: center; font-size: 23px; letter-spacing: 2px; }
  .speaker { position: absolute; top: 495px; width: 144px; }
  .speaker-frame { width: 144px; height: 226px; padding: 5px 5px 14px; }
  .speaker-photo { width: 100%; height: 100%; }
  .speaker-name {
    position: absolute; top: 234px; left: -10px; width: 164px; height: 28px;
    text-align: center; font-size: 23px; line-height: 28px; white-space: nowrap;
  }
  .speaker-high { left: 34px; }
  .speaker-high .speaker-frame { background: #000; }
  .speaker-high .speaker-photo { background: linear-gradient(160deg, #3f5a2e, #8fb0d8 60%, #2d3a55); }
  .speaker-high .speaker-name { background: var(--slate); }
  .speaker-middle { left: 274px; }
  .speaker-middle .speaker-frame { background: var(--magenta); }
  .speaker-middle .speaker-photo { background: linear-gradient(180deg, #4a4a4e, #8c7a70 50%, #2a1a1c); }
  .speaker-middle .speaker-name { background: var(--magenta); }
  .speaker-ignite { left: 490px; }
  .speaker-ignite .speaker-frame { background: var(--violet); }
  .speaker-ignite .speaker-photo { background: linear-gradient(180deg, #b8a488, #c9a07a 45%, #9a8aa0); }
  .speaker-ignite .speaker-name { background: var(--violet); }
  .logo { position: absolute; left: 0; width: 100%; top: 808px; display: flex; justify-content: center; align-items: center; gap: 10px; font-size: 30px; font-weight: 700; color: var(--logo-blue); }
  .logo-dot { width: 18px; height: 18px; border-radius: 50%; background: var(--logo-blue); }
  .venue { position: absolute; left: 0; width: 100%; top: 891px; text-align: center; font-size: 19px; }
</style>
</head>
<body>
<main class="poster">
  <svg class="backdrop" viewBox="0 0 674 953" aria-hidden="true">
    <defs>
      <radialGradient id="glow-pink" cx="0.1" cy="0.3" r="0.6">
        <stop offset="0" stop-color="#d02a8a" stop-opacity="0.85"/>
        <stop offset="1" stop-color="#d02a8a" stop-opacity="0"/>
      </radialGradient>
      <radialGradient id="glow-purple" cx="0.25" cy="0.55" r="0.6">
        <stop offset="0" stop-color="#8a3ad8" stop-opacity="0.85"/>
        <stop offset="1" stop-color="#8a3ad8" stop-opacity="0"/>
      </radialGradient>
      <radialGradient id="glow-blue" cx="0.2" cy="0.85" r="0.65">
        <stop offset="0" stop-color="#2a3ae0" stop-opacity="0.9"/>
        <stop offset="1" stop-color="#2a3ae0" stop-opacity="0"/>
      </radialGradient>
    </defs>
    <rect width="674" height="953" fill="url(#glow-pink)"/>
    <rect width="674" height="953" fill="url(#glow-purple)"/>
    <rect width="674" height="953" fill="url(#glow-blue)"/>
    <g fill="#ffffff" opacity="0.1">
      <polygon points="40,20 110,130 -30,130"/>
      <polygon points="0,230 90,230 0,360"/>
      <polygon points="55,395 120,500 -10,500"/>
      <polygon points="150,700 230,830 70,830"/>
      <polygon points="40,800 110,920 -30,920"/>
      <polygon points="230,860 300,960 160,960"/>
    </g>
    <circle cx="150" cy="790" r="5" fill="#7fb0ff" opacity="0.9"/>
    <circle cx="640" cy="150" r="4" fill="#b06ad0" opacity="0.8"/>
  </svg>

  <h1>
    <span class="title title-brand">PINE RIDGE YOUTH</span>
    <span class="title title-summer">SUMMER</span>
    <span class="title title-camps">CAMPS</span>
  </h1>

  <p class="schedule">
    <b>HIGH SCHOOL</b> | JUNE 3-7<br>
    <b>MIDDLE SCHOOL</b> | JUNE 17-21<br>
    <b>IGNITE</b> | JUNE 24 - 28
  </p>
  <p class="register">Register at PineRidgeYouth.com</p>

  <figure class="speaker speaker-high">
    <div class="speaker-frame"><div class="speaker-photo" role="img" aria-label="Headshot of speaker Ray Whitcomb"></div></div>
    <figcaption class="speaker-name">Ray Whitcomb</figcaption>
  </figure>
  <figure class="speaker speaker-middle">
    <div class="speaker-frame"><div class="speaker-photo" role="img" aria-label="Headshot of speaker Marla Pettis"></div></div>
    <figcaption class="speaker-name">Marla Pettis</figcaption>
  </figure>
  <figure class="speaker speaker-ignite">
    <div class="speaker-frame"><div class="speaker-photo" role="img" aria-label="Headshot of speaker Cody Brandt"></div></div>
    <figcaption class="speaker-name">Cody Brandt</figcaption>
  </figure>

  <div class="logo"><span class="logo-dot"></span>Pine Ridge Youth</div>
  <p class="venue">Cedar Hollow Retreat Center, Aspen Falls, WY</p>
</main>
</body>
</html>
```